create clean, simple business card template

using the logo created now we need to create a simple, elegant business card design to suit

Industry/Entity Type

Business

Font styles to use
Other font styles liked:
• segoe ui

Requirements
Must have
• Front:
"Name:"
"Title:"
"Mobile:"
"email:"
and the logo

Back:
Logo
Nice to have
• Text in black but other graphics etc to match colours in logo as provided

```html
<!DOCTYPE html>
<html lang="en">
<head>
<meta charset="utf-8">
<title>Halden Estates – Business Cards</title>
<link rel="stylesheet" href="https://fonts.googleapis.com/css2?family=Open+Sans:wght@400;600;700&display=swap">
<style>
  :root {
    --page-bg: #ecebe8;
    --card-white: #f7f7f6;
    --card-shade: #e4e4e3;
    --gold: #8a6f3e;
    --gold-dark: #6b5430;
    --ink: #2b2b2b;
    --ink-soft: #4a4a4a;
    --charcoal: #2f2f2f;
  }
  * { box-sizing: border-box; margin: 0; padding: 0; }
  html, body { width: 1200px; height: 1000px; overflow: hidden; }
  body {
    background: var(--page-bg);
    font-family: "Open Sans", "Segoe UI", sans-serif;
    position: relative;
  }
  .card {
    position: absolute;
    width: 540px;
    height: 310px;
    border-radius: 4px;
    overflow: hidden;
    box-shadow: 0 10px 28px rgba(0,0,0,0.18);
  }
  .card-back {
    left: 70px; top: 150px;
    background: linear-gradient(160deg, var(--card-shade) 0%, var(--card-white) 55%);
  }
  .card-front {
    left: 590px; top: 520px;
    background: var(--card-white);
    border-right: 6px solid var(--gold);
  }
  .swoosh { position: absolute; inset: 0; width: 100%; height: 100%; }
  .brand {
    position: absolute;
    display: flex;
    align-items: center;
    gap: 14px;
  }
  .brand-dot {
    width: 34px; height: 34px;
    border-radius: 50%;
    background: var(--charcoal);
  }
  .brand-name {
    font-weight: 600;
    font-size: 30px;
    color: var(--gold);
    letter-spacing: 0.5px;
  }
  .card-back .brand { left: 110px; top: 112px; }
  .card-front .brand { left: 125px; top: 60px; }
  .holder {
    position: absolute;
    left: 40px; bottom: 48px;
  }
  .holder-name {
    font-weight: 700;
    font-size: 26px;
    color: var(--gold);
    line-height: 1.1;
  }
  .holder-title {
    font-size: 15px;
    color: var(--ink-soft);
    margin-top: 4px;
  }
  .divider {
    position: absolute;
    left: 268px; bottom: 42px;
    width: 1px; height: 80px;
    background: var(--gold);
  }
  .contact {
    position: absolute;
    right: 30px; bottom: 58px;
    list-style: none;
    text-align: right;
    font-size: 14px;
    color: var(--ink);
  }
  .contact li {
    display: flex;
    justify-content: flex-end;
    align-items: center;
    gap: 8px;
    margin-top: 8px;
  }
  .contact svg { width: 15px; height: 15px; fill: var(--gold-dark); }
</style>
</head>
<body>

  <section class="card card-back" aria-label="Card back">
    <svg class="swoosh" viewBox="0 0 540 310" preserveAspectRatio="none" aria-hidden="true">
      <path d="M0 250 C 170 300, 400 270, 540 110 L 540 122 C 400 282, 170 312, 0 262 Z" fill="var(--gold)"/>
    </svg>
    <div class="brand">
      <span class="brand-dot"></span>
      <span class="brand-name">Halden Estates</span>
    </div>
  </section>

  <section class="card card-front" aria-label="Card front">
    <div class="brand">
      <span class="brand-dot"></span>
      <span class="brand-name">Halden Estates</span>
    </div>

    <div class="holder">
      <p class="holder-name">Mark Ellison</p>
      <p class="holder-title">Property Manager</p>
    </div>

    <span class="divider"></span>

    <ul class="contact">
      <li>+ 555 - 0142 - 7788 :
        <svg viewBox="0 0 24 24" aria-label="Phone"><path d="M6.6 10.8a15 15 0 0 0 6.6 6.6l2.2-2.2c.3-.3.7-.4 1-.2 1.1.4 2.3.6 3.6.6.6 0 1 .4 1 1V20c0 .6-.4 1-1 1A17 17 0 0 1 3 4c0-.6.4-1 1-1h3.5c.6 0 1 .4 1 1 0 1.3.2 2.5.6 3.6.1.3 0 .7-.2 1z"/></svg>
      </li>
      <li>mark@haldenestates.com :
        <svg viewBox="0 0 24 24" aria-label="Email"><path d="M2 5h20v14H2z M3 6l9 7 9-7" fill="none" stroke="var(--gold-dark)" stroke-width="2"/></svg>
      </li>
    </ul>
  </section>

</body>
</html>
```